Creative Workshop Business needs a Promotional flyer

We need a promotional brochure for our business. We will provide you with the copy to include in the brochure. The look were are trying to achieve is clean, less is more and provide crisp visuals to communicate our message. We would like you to think outside the box in your design but remember we are a kids creative craft and art workshop business - so fun but not too kiddie! We have attached our logo, images to use and examples (marked examples #1 etc) that we love. Once this brochure has been created we would like to continue to work with the designer to create our marketing suite for our business. We have attached a lo res design of our trailer signage as an example and maybe a place to start designing.
When using the logo please not that the wording "CREATIVE WORKSHOPS IS REPLACED WITH CREATIVE WORKSHOPS FOR KIDS".
We have attached our font as well but are happy for suggestions on font.
If there is any clarification needed please contact tara@pebblehollowarts.com.au

• Font has been provided

• Great visuals and use the images provided.
• Easy to read and follow but more than your usually tri-fold design. We want customers to pick up our flyer above anyone else'.

```html
<!DOCTYPE html>
<html lang="en">
<head>
<meta charset="utf-8">
<title>Creative Workshops for Kids – What You Receive</title>
<link rel="stylesheet" href="https://fonts.googleapis.com/css2?family=Josefin+Sans:wght@400;600&display=swap">
<style>
  :root {
    --paper: #ffffff;
    --ink-blue: #1c5a9c;
    --paint-blue: #2a9fd0;
    --paint-light: #e9eef2;
    --skin-warm: #d9a98a;
    --shirt-blue: #8fb7d8;
    --mobile-pink: #f2a6c8;
    --mobile-haze: #c9c2c6;
  }
  * { box-sizing: border-box; margin: 0; padding: 0; }
  html, body {
    width: 1200px;
    height: 1200px;
    overflow: hidden;
    background: var(--paper);
  }
  .panel {
    position: relative;
    width: 1200px;
    height: 1200px;
    background: var(--paper);
    overflow: hidden;
    font-family: "Josefin Sans", sans-serif;
    color: var(--ink-blue);
  }
  .photo-frames {
    position: absolute;
    inset: 0;
  }
  .benefits {
    position: absolute;
    left: 390px;
    font-variant: small-caps;
    letter-spacing: 0.04em;
  }
  .benefits h2 {
    font-weight: 400;
    font-size: 30px;
    line-height: 1;
  }
  .benefits ul {
    list-style: none;
    margin-top: 22px;
  }
  .benefits li {
    position: relative;
    padding-left: 22px;
    font-size: 23px;
  }
  .benefits li::before {
    content: "";
    position: absolute;
    left: 4px;
    top: 14px;
    width: 5px;
    height: 5px;
    border-radius: 50%;
    background: var(--ink-blue);
  }
  .for-children { top: 598px; }
  .for-children li { line-height: 37.6px; }
  .for-parents { top: 847px; }
  .for-parents ul { margin-top: 46px; }
  .for-parents li { line-height: 33.7px; }
</style>
</head>
<body>
<main class="panel">
  <svg class="photo-frames" width="1200" height="1200" viewBox="0 0 1200 1200">
    <defs>
      <radialGradient id="paint-tray-tones" cx="0.55" cy="0.55" r="0.6">
        <stop offset="0" stop-color="var(--paint-blue)"/>
        <stop offset="0.55" stop-color="#6fc0e2"/>
        <stop offset="1" stop-color="var(--paint-light)"/>
      </radialGradient>
      <linearGradient id="mobile-tones" x1="0" y1="0" x2="1" y2="1">
        <stop offset="0" stop-color="var(--mobile-haze)"/>
        <stop offset="0.6" stop-color="var(--mobile-pink)"/>
        <stop offset="1" stop-color="#f6d9e6"/>
      </linearGradient>
      <linearGradient id="child-tones" x1="0" y1="0" x2="0" y2="1">
        <stop offset="0" stop-color="#eef0f2"/>
        <stop offset="0.45" stop-color="var(--skin-warm)"/>
        <stop offset="1" stop-color="var(--shirt-blue)"/>
      </linearGradient>
    </defs>
    <circle class="photo paint-roller" cx="354" cy="255" r="331" fill="url(#paint-tray-tones)"
            role="img" aria-label="Photo: a child's hand rolling a paint roller through a tray of bright blue paint"/>
    <circle class="photo paper-mobile" cx="975" cy="201" r="230" fill="url(#mobile-tones)"
            role="img" aria-label="Photo: a hanging craft mobile of pink drinking straws and pink, yellow and white paper flowers"/>
    <circle class="photo young-artist" cx="-26" cy="670" r="382" fill="url(#child-tones)"
            role="img" aria-label="Photo: a young boy in a blue polo shirt concentrating on his craft project"/>
  </svg>

  <section class="benefits for-children">
    <h2>Your children receive</h2>
    <ul>
      <li>All materials Guidance and encouragement</li>
      <li>A safe community environment where they can interact with<br>others and let their creativity flow with no fear or judgment</li>
      <li>Confidence building enabling your children to<br>make decisions without guidance.</li>
    </ul>
  </section>

  <section class="benefits for-parents">
    <h2>You receive</h2>
    <ul>
      <li>Peace of mind that your child is fully supervised in a safe<br>environment</li>
      <li>Time to yourself while your child explores their creativity.<br>Now who doesn't love a relaxing cup of coffee?!</li>
      <li>A quality piece of artwork that you're proud to display in<br>your home.</li>
      <li>A satisfied, fulfilled and happy child.</li>
    </ul>
  </section>
</main>
</body>
</html>
```